Infografik für unabhängigen Finanzdienstleister
Zielgruppe
Wir sind eine unabhängiger Finanzdienstleister mit dem Schwerpunkt der Kapitalanlage und dem Fokus auf vermögende Privatkunden. Wir sind nur unseren Mandanten verpflichtet, da diese unsere Dienstleistung transparent und frei von versteckten Provisionen honorieren.
Aufgabenstellung
Klassisch modern, aber nicht verspielt. Ein Gefühl gibt unsere Homepage. Weitere Infos zum Projekt habe ich hier in einem kurzen Video verfasst: https://lobark.vemiko-kanzlei.example/message?id=7f91c3a5e2d04b
Ergänzung:
Die Grafik soll sich mehr 'selbst erklären lassen' als sie es derzeit tut. Zudem soll die Prozessreihenfolge besser verdeutlicht werden...

```html
<!DOCTYPE html>
<html lang="de">
<head>
<meta charset="utf-8">
<title>Infografik – Unabhängige Finanzberatung</title>
<link rel="stylesheet" href="https://fonts.googleapis.com/css2?family=Cinzel:wght@500&family=Oswald:wght@500;700&family=Questrial&display=swap">
<style>
  :root {
    --paper: #ffffff;
    --top-dark: #5e3a22;
    --top-mid: #8c5a3a;
    --top-light: #9d6c3b;
    --top-band: #b1853d;
    --top-wedge: #6d402e;
    --top-title: #4b2e12;
    --top-numeral: #b58a3e;

    --red-upper: #c8171f;
    --red-lower: #a10d14;
    --red-deep: #780a0c;
    --red-band: #ed1b36;
    --red-wedge: #8b2a31;
    --red-inner-right: #a60d15;
    --red-title: #6d0b12;
    --red-numeral: #c22a30;

    --green-upper: #05482f;
    --green-lower: #2a5e45;
    --green-bottom: #1a7449;
    --green-band: #1fa36a;
    --green-wedge: #1e5d43;
    --green-inner: #0a6c45;
    --green-title: #0c3e2a;

    --lens-red-top: #a8232b;
    --lens-green-top: #3a6b43;
    --lens-core: #56333b;

    --badge-ring: #ffffff;
    --badge-text: #111111;
    --label: #ffffff;
    --lens-label: #f6e4e4;
  }
  html, body {
    margin: 0;
    padding: 0;
    width: 1200px;
    height: 1200px;
    overflow: hidden;
    background: var(--paper);
  }
  .infographic {
    display: block;
    width: 1200px;
    height: 1200px;
  }
  .ring-label {
    font-family: "Questrial", sans-serif;
    font-size: 30px;
    fill: var(--label);
    text-anchor: middle;
  }
  .stage-title {
    font-family: "Oswald", sans-serif;
    font-weight: 700;
    text-anchor: middle;
  }
  .stage-title--top { fill: var(--top-title); }
  .stage-title--red { fill: var(--red-title); font-size: 38px; }
  .stage-title--green { fill: var(--green-title); font-size: 38px; }
  .numeral {
    font-family: "Cinzel", serif;
    font-weight: 500;
    font-size: 50px;
    text-anchor: middle;
    dominant-baseline: central;
  }
  .lens-label {
    font-family: "Questrial", sans-serif;
    font-size: 18px;
    letter-spacing: 0.5px;
    fill: var(--lens-label);
    text-anchor: middle;
  }
  .lens-label--core { font-size: 19px; }
  .badge-label {
    font-family: "Oswald", sans-serif;
    font-weight: 700;
    font-size: 19px;
    letter-spacing: 1px;
    fill: var(--badge-text);
    text-anchor: middle;
  }
</style>
</head>
<body>
<svg class="infographic" viewBox="0 0 1575 1575" xmlns="http://www.w3.org/2000/svg" role="img" aria-label="Drei Phasen der Finanzbegleitung: Starkes Fundament, Nachhaltige Umsetzung, Aktive Begleitung und Optimierung">
  <defs>
    <radialGradient id="badge-core-glow" cx="50%" cy="45%" r="55%">
      <stop offset="0%" stop-color="#f9a21b"/>
      <stop offset="55%" stop-color="#c8761c"/>
      <stop offset="100%" stop-color="#4a2a16"/>
    </radialGradient>

    <clipPath id="clip-left-half"><rect x="0" y="0" width="789" height="1575"/></clipPath>
    <clipPath id="clip-right-half"><rect x="789" y="0" width="786" height="1575"/></clipPath>
    <clipPath id="clip-top-band"><circle cx="789" cy="621" r="303"/></clipPath>
    <clipPath id="clip-red-band"><circle cx="610" cy="935" r="303"/></clipPath>

    <!-- upper arcs, clockwise, glyph tops point outward -->
    <path id="arc-up-400" d="M -393.92 -69.46 A 400 400 0 0 1 393.92 -69.46"/>
    <path id="arc-up-390" d="M -384.08 -67.72 A 390 390 0 0 1 384.08 -67.72"/>
    <path id="arc-up-362" d="M -356.50 -62.86 A 362 362 0 0 1 356.50 -62.86"/>
    <path id="arc-up-324" d="M -319.08 -56.26 A 324 324 0 0 1 319.08 -56.26"/>

    <!-- lower arcs, counter-clockwise, glyph tops point inward -->
    <path id="arc-down-205" d="M -201.89 35.60 A 205 205 0 0 0 201.89 35.60"/>
    <path id="arc-down-258" d="M -254.08 44.80 A 258 258 0 0 0 254.08 44.80"/>
    <path id="arc-down-340" d="M -334.84 59.04 A 340 340 0 0 0 334.84 59.04"/>
    <path id="arc-down-372" d="M -366.35 64.60 A 372 372 0 0 0 366.35 64.60"/>
    <path id="arc-down-378" d="M -372.26 65.64 A 378 378 0 0 0 372.26 65.64"/>
    <path id="arc-down-408" d="M -401.80 70.85 A 408 408 0 0 0 401.80 70.85"/>
    <path id="arc-down-410" d="M -403.77 71.20 A 410 410 0 0 0 403.77 71.20"/>
    <path id="arc-down-416" d="M -409.68 72.24 A 416 416 0 0 0 409.68 72.24"/>

    <path id="arc-title-line1" d="M 569 484 A 400 400 0 0 1 1009 484"/>
    <path id="arc-title-line2" d="M 569 519 A 520 520 0 0 1 1009 519"/>

    <path id="arc-badge-top" d="M 723.25 835.75 A 66 66 0 1 1 854.75 835.75"/>
    <path id="arc-badge-bottom" d="M 705.32 837.32 A 84 84 0 0 0 872.68 837.32"/>
  </defs>

  <!-- outer service rings -->
  <g class="outer-ring outer-ring--top">
    <path fill="var(--top-dark)" d="M789 621 L407.95 841 A440 440 0 0 1 569 239.96 Z"/>
    <path fill="var(--top-mid)" d="M789 621 L569 239.96 A440 440 0 0 1 1009 239.96 Z"/>
    <path fill="var(--top-light)" d="M789 621 L1009 239.96 A440 440 0 0 1 1170.05 841 Z"/>
  </g>
  <g class="outer-ring outer-ring--red" clip-path="url(#clip-left-half)">
    <path fill="var(--red-upper)" d="M610 935 L170 935 A440 440 0 0 1 686.4 501.7 Z"/>
    <path fill="var(--red-lower)" d="M610 935 L390 1316.05 A440 440 0 0 1 170 935 Z"/>
    <path fill="var(--red-deep)" d="M610 935 L947.1 1217.8 A440 440 0 0 1 390 1316.05 Z"/>
  </g>
  <g class="outer-ring outer-ring--green" clip-path="url(#clip-right-half)">
    <path fill="var(--green-upper)" d="M968 935 L891.6 501.7 A440 440 0 0 1 1408 935 Z"/>
    <path fill="var(--green-lower)" d="M968 935 L1408 935 A440 440 0 0 1 1188 1316.05 Z"/>
    <path fill="var(--green-bottom)" d="M968 935 L1188 1316.05 A440 440 0 0 1 630.9 1217.8 Z"/>
  </g>

  <!-- stage bands -->
  <g class="stage-band">
    <circle cx="789" cy="621" r="303" fill="var(--top-band)"/>
    <circle cx="610" cy="935" r="303" fill="var(--red-band)"/>
    <circle cx="968" cy="935" r="303" fill="var(--green-band)"/>
  </g>

  <!-- stage hubs -->
  <g class="stage-hub stage-hub--top">
    <path fill="var(--top-wedge)" d="M789 621 L719.5 500.6 A139 139 0 0 1 858.5 500.6 Z"/>
    <path fill="var(--top-light)" d="M789 621 L858.5 500.6 A139 139 0 0 1 858.5 741.4 Z"/>
    <path fill="var(--top-mid)" d="M789 621 L858.5 741.4 A139 139 0 0 1 719.5 741.4 Z"/>
    <path fill="var(--top-dark)" d="M789 621 L719.5 741.4 A139 139 0 0 1 719.5 500.6 Z"/>
  </g>
  <g class="stage-hub stage-hub--red">
    <path fill="var(--red-wedge)" d="M610 935 L540.5 1055.4 A139 139 0 0 1 471 935 Z"/>
    <path fill="var(--red-upper)" d="M610 935 L471 935 A139 139 0 0 1 679.5 814.6 Z"/>
    <path fill="var(--red-inner-right)" d="M610 935 L679.5 814.6 A139 139 0 0 1 749 935 Z"/>
    <path fill="var(--red-deep)" d="M610 935 L749 935 A139 139 0 0 1 540.5 1055.4 Z"/>
  </g>
  <g class="stage-hub stage-hub--green">
    <path fill="var(--green-upper)" d="M968 935 L898.5 814.6 A139 139 0 0 1 1107 935 Z"/>
    <path fill="var(--green-wedge)" d="M968 935 L1107 935 A139 139 0 0 1 1026.7 1061 Z"/>
    <path fill="var(--green-inner)" d="M968 935 L1026.7 1061 A139 139 0 0 1 898.5 814.6 Z"/>
  </g>

  <!-- overlaps -->
  <g class="overlap">
    <circle cx="610" cy="935" r="303" fill="var(--lens-red-top)" clip-path="url(#clip-top-band)"/>
    <circle cx="968" cy="935" r="303" fill="var(--lens-green-top)" clip-path="url(#clip-top-band)"/>
    <circle cx="968" cy="935" r="303" fill="var(--lens-core)" clip-path="url(#clip-red-band)"/>
  </g>

  <!-- stage numerals -->
  <text class="numeral" x="789" y="540" fill="var(--top-numeral)">III</text>
  <text class="numeral" x="530" y="975" fill="var(--red-numeral)" transform="rotate(60 530 975)">I</text>
  <text class="numeral" x="1050" y="970" fill="var(--green-wedge)" transform="rotate(-60 1050 970)" style="fill:#0d4a33">II</text>

  <!-- stage titles -->
  <text class="stage-title stage-title--top" font-size="46"><textPath href="#arc-title-line1" startOffset="50%" textLength="330" lengthAdjust="spacingAndGlyphs">AKTIVE BEGLEITUNG</textPath></text>
  <text class="stage-title stage-title--top" font-size="36"><textPath href="#arc-title-line2" startOffset="50%" textLength="250" lengthAdjust="spacingAndGlyphs">UND OPTIMIERUNG</textPath></text>

  <g transform="translate(610 935) rotate(60)">
    <text class="stage-title stage-title--red" letter-spacing="16"><textPath href="#arc-down-205" startOffset="50%">STARKES</textPath></text>
    <text class="stage-title stage-title--red" letter-spacing="17"><textPath href="#arc-down-258" startOffset="50%">FUNDAMENT</textPath></text>
  </g>
  <g transform="translate(968 935) rotate(-60)">
    <text class="stage-title stage-title--green" letter-spacing="3"><textPath href="#arc-down-205" startOffset="50%">NACHHALTIGE</textPath></text>
    <text class="stage-title stage-title--green" letter-spacing="16"><textPath href="#arc-down-258" startOffset="50%">UMSETZUNG</textPath></text>
  </g>

  <!-- outer ring labels: top stage -->
  <g transform="translate(789 621)">
    <text class="ring-label"><textPath href="#arc-up-400" startOffset="50%">Notfallplan</textPath></text>
  </g>
  <g transform="translate(789 621) rotate(-55)">
    <text class="ring-label"><textPath href="#arc-up-400" startOffset="50%">Zentraler</textPath></text>
    <text class="ring-label"><textPath href="#arc-up-362" startOffset="50%">Ansprechpartner zum</textPath></text>
    <text class="ring-label"><textPath href="#arc-up-324" startOffset="50%">Thema Finanzen</textPath></text>
  </g>
  <g transform="translate(789 621) rotate(57.5)">
    <text class="ring-label"><textPath href="#arc-up-390" startOffset="50%">Experten-Netzwerk</textPath></text>
  </g>

  <!-- outer ring labels: red stage -->
  <g transform="translate(610 935) rotate(-67)">
    <text class="ring-label"><textPath href="#arc-up-400" startOffset="50%">Entwicklung eines</textPath></text>
    <text class="ring-label"><textPath href="#arc-up-362" startOffset="50%">persönlichen</textPath></text>
    <text class="ring-label"><textPath href="#arc-up-324" startOffset="50%">Finanzplans</textPath></text>
  </g>
  <g transform="translate(610 935) rotate(60.5)">
    <text class="ring-label"><textPath href="#arc-down-408" startOffset="50%">Wissensvermittlung</textPath></text>
  </g>
  <g transform="translate(610 935)">
    <text class="ring-label" transform="rotate(1)"><textPath href="#arc-down-340" startOffset="50%">Tiefe Analyse Ihrer</textPath></text>
    <text class="ring-label" transform="rotate(6)"><textPath href="#arc-down-378" startOffset="50%">IST-Situation und</textPath></text>
    <text class="ring-label" transform="rotate(14)"><textPath href="#arc-down-416" startOffset="50%">Ihrer Ziele</textPath></text>
  </g>

  <!-- outer ring labels: green stage -->
  <g transform="translate(968 935) rotate(65)">
    <text class="ring-label"><textPath href="#arc-up-400" startOffset="50%">Transparente und</textPath></text>
    <text class="ring-label"><textPath href="#arc-up-362" startOffset="50%">provisionsfreie</textPath></text>
    <text class="ring-label"><textPath href="#arc-up-324" startOffset="50%">Vergütung</textPath></text>
  </g>
  <g transform="translate(968 935) rotate(-61.5)">
    <text class="ring-label"><textPath href="#arc-down-372" startOffset="50%">Berücksichtigung</textPath></text>
    <text class="ring-label"><textPath href="#arc-down-410" startOffset="50%">steuerlicher Aspekte</textPath></text>
  </g>
  <g transform="translate(968 935)">
    <text class="ring-label" transform="rotate(0.5)"><textPath href="#arc-down-340" startOffset="50%">Nobelpreisgekrönte</textPath></text>
    <text class="ring-label" transform="rotate(-5.6)"><textPath href="#arc-down-378" startOffset="50%">und erfolgreiche</textPath></text>
    <text class="ring-label" transform="rotate(-8.3)"><textPath href="#arc-down-416" startOffset="50%">Anlagestrategie</textPath></text>
  </g>

  <!-- overlap labels -->
  <g transform="translate(635 740) rotate(-57)">
    <text class="lens-label" y="-51">UMFASSENDER</text>
    <text class="lens-label" y="-13">SCHUTZ VON</text>
    <text class="lens-label" y="25">VERMÖGEN</text>
    <text class="lens-label" y="63">UND FAMILIE</text>
  </g>
  <g transform="translate(966 727) rotate(60)">
    <text class="lens-label" y="-34">WENIGER</text>
    <text class="lens-label" y="6">VERWALTUNG,</text>
    <text class="lens-label" y="46">MEHR ZEIT</text>
  </g>
  <g class="core-label">
    <text class="lens-label lens-label--core" x="789" y="972">FINANZIELLER</text>
    <text class="lens-label lens-label--core" x="789" y="1010">ERFOLG / GUTE</text>
    <text class="lens-label lens-label--core" x="789" y="1049">INVESTMENTER</text>
    <text class="lens-label lens-label--core" x="789" y="1089">FAHRUNG</text>
  </g>

  <!-- client badge -->
  <g class="client-badge">
    <circle cx="789" cy="830" r="96" fill="var(--badge-ring)"/>
    <circle cx="789" cy="830" r="56" fill="#3a2418"/>
    <circle cx="789" cy="830" r="52" fill="url(#badge-core-glow)"/>
    <text class="badge-label"><textPath href="#arc-badge-top" startOffset="50%">UNTERNEHMER/IN</textPath></text>
    <text class="badge-label"><textPath href="#arc-badge-bottom" startOffset="50%">FREIBERUFLER / IN</textPath></text>
  </g>
</svg>
</body>
</html>
```